innovative investment real estate sales firm

We are a uniquely collabrative firm that seeks to bring a conultative approach to uncovering hidden opportunities for our clients, our website needs to convey our client focused approach. Our firm specializes in the sale of apartment properties in Southern California. We have a team of researchers, transaction coordinators and marketing personal to support our geographically specialized advisers. We need a website that introduces clients to our unique way of better helping them achieve their investment goals.

Target Market(s)

High net worth individuals and families

Industry/Entity Type

Real Estate Agent

Font styles to use
Other font styles liked:
• please use font provided

Requirements
Must have
• Stories of our recent projects
• Features on our people
• email capture for viewing inventory
• content that showcases our unique consultative approach that uncovers unrealized opportunities

```html
<!DOCTYPE html>
<html lang="en">
<head>
<meta charset="utf-8">
<title>Meridian Advisers — Multifamily Properties</title>
<link href="https://fonts.googleapis.com/css2?family=Montserrat:wght@500;600;700&family=Open+Sans:wght@400;600&display=swap" rel="stylesheet">
<style>
  :root {
    --teal: #0aa1b9;
    --green: #9bcb0b;
    --ink: #3b4450;
    --text: #555c63;
    --muted: #6e747a;
    --band: #f2f2f2;
    --footer: #454d57;
    --white: #ffffff;
    --line: #c9cccf;
  }
  * { box-sizing: border-box; margin: 0; padding: 0; }
  html, body { width: 1200px; height: 2353px; overflow: hidden; }
  body { position: relative; background: var(--white); font-family: "Open Sans", Arial, sans-serif; color: var(--text); }
  .abs { position: absolute; }
  .heading { font-family: "Montserrat", Arial, sans-serif; font-weight: 600; text-transform: uppercase; }

  /* Header */
  .site-header { left: 0; top: 0; width: 1200px; height: 137px; }
  .brand { left: 132px; top: 44px; display: flex; align-items: center; gap: 14px; }
  .brand-mark { width: 44px; height: 44px; background: var(--teal); }
  .brand-name { font-family: "Montserrat", Arial, sans-serif; font-weight: 600; font-size: 26px; color: var(--ink); letter-spacing: 1px; text-transform: uppercase; }
  .main-nav { right: 133px; top: 63px; display: flex; gap: 27px; font-family: "Montserrat", Arial, sans-serif; font-weight: 500; font-size: 13.5px; color: var(--ink); text-transform: uppercase; }
  .main-nav .active { color: var(--teal); }

  /* Hero */
  .hero { left: 0; top: 137px; width: 1200px; height: 478px; background: linear-gradient(100deg, #1d3e7a 0%, #3f7fd9 30%, #6aa6f0 48%, #2f7cf0 70%, #0d5cf5 100%); }
  .hero-buildings { left: 0; top: 0; width: 1200px; height: 478px; }
  .hero-copy { right: 133px; top: 257px; text-align: right; color: var(--white); }
  .hero-copy .line { font-family: "Montserrat", Arial, sans-serif; font-weight: 500; font-size: 20px; line-height: 27px; color: #cfe0f7; text-transform: uppercase; }
  .hero-copy .place { font-family: "Montserrat", Arial, sans-serif; font-weight: 600; font-size: 26px; line-height: 40px; text-transform: uppercase; }
  .btn-contact { right: 133px; top: 358px; width: 145px; height: 47px; background: #3a3f45; color: var(--white); font-family: "Montserrat", Arial, sans-serif; font-weight: 600; font-size: 16px; display: flex; align-items: center; justify-content: center; text-transform: uppercase; }
  .slider-arrow { width: 20px; height: 30px; }

  /* Approach */
  .approach { left: 132px; top: 683px; width: 935px; text-align: center; }
  .section-title { font-family: "Montserrat", Arial, sans-serif; font-weight: 600; font-size: 33px; color: var(--teal); text-transform: uppercase; }
  .approach .subtitle { margin-top: 6px; font-size: 17px; color: var(--ink); }
  .approach p { margin-top: 10px; font-size: 12.4px; line-height: 19.7px; color: var(--text); }

  /* Features */
  .features { left: 0; top: 918px; width: 1200px; height: 310px; background: var(--band); }
  .feature { top: 58px; width: 300px; text-align: center; }
  .feature-icon { width: 96px; height: 96px; border-radius: 50%; background: var(--green); margin: 0 auto; display: flex; align-items: center; justify-content: center; }
  .feature h3 { margin-top: 26px; font-size: 17px; color: var(--ink); }
  .feature p { margin-top: 6px; font-size: 11.2px; line-height: 17px; color: var(--text); }

  /* Projects */
  .projects-title { left: 0; top: 1300px; width: 1200px; text-align: center; }
  .project { top: 1357px; width: 298px; }
  .project-photo { width: 298px; height: 201px; }
  .project h3 { margin-top: 16px; font-size: 16px; color: var(--ink); }
  .project p { margin-top: 9px; font-size: 11.2px; line-height: 17px; color: var(--text); }
  .btn-more { margin-top: 17px; width: 80px; height: 35px; border: 1px solid var(--line); font-size: 10.5px; color: var(--muted); display: flex; align-items: center; justify-content: center; }

  /* People */
  .people { left: 0; top: 1801px; width: 1200px; height: 361px; background: var(--band); }
  .people-title { left: 0; top: 71px; width: 1200px; text-align: center; }
  .person { top: 135px; width: 160px; text-align: center; }
  .portrait { width: 96px; height: 96px; border-radius: 50%; margin: 0 auto; background: radial-gradient(circle at 50% 40%, #d9d6d2 0%, #a9a7a5 60%, #6a6c70 100%); }
  .person .name { margin-top: 12px; font-size: 16px; color: var(--ink); }
  .person .role { margin-top: 2px; font-size: 11px; color: var(--text); }

  /* Newsletter */
  .newsletter { left: 0; top: 2162px; width: 1200px; height: 95px; background: var(--teal); }
  .newsletter-title { left: 132px; top: 28px; display: flex; align-items: center; gap: 12px; color: var(--white); font-family: "Montserrat", Arial, sans-serif; font-weight: 700; font-size: 31px; text-transform: uppercase; }
  .field { top: 28px; width: 256px; height: 39px; background: var(--white); font-size: 11px; color: #9aa0a5; padding-left: 14px; display: flex; align-items: center; }
  .btn-subscribe { left: 940px; top: 28px; width: 127px; height: 39px; background: var(--green); color: var(--white); font-family: "Montserrat", Arial, sans-serif; font-weight: 700; font-size: 15px; display: flex; align-items: center; justify-content: center; text-transform: uppercase; }

  /* Footer */
  .site-footer { left: 0; top: 2257px; width: 1200px; height: 96px; background: var(--footer); color: var(--white); }
  .footer-nav { left: 132px; top: 27px; font-size: 11px; }
  .footer-nav span.sep { margin: 0 8px; }
  .copyright { left: 132px; top: 52px; font-size: 11px; }
  .social { top: 42px; width: 16px; height: 16px; border-radius: 50%; background: #d9dde1; }
</style>
</head>
<body>

<header class="site-header abs">
  <div class="brand abs"><span class="brand-mark"></span><span class="brand-name">Meridian Advisers</span></div>
  <nav class="main-nav abs">
    <span class="active">Home</span><span>About us</span><span>Projects</span><span>How we work?</span><span>Contact</span>
  </nav>
</header>

<section class="hero abs">
  <div class="hero-buildings abs" role="img" aria-label="Modern glass apartment buildings lit at dusk against a blue sky"></div>
  <svg class="slider-arrow abs" style="left:22px;top:224px" viewBox="0 0 20 30"><path d="M15 3 L4 15 L15 27" fill="none" stroke="#ffffff" stroke-width="2.5"/></svg>
  <svg class="slider-arrow abs" style="left:1159px;top:224px" viewBox="0 0 20 30"><path d="M5 3 L16 15 L5 27" fill="none" stroke="#ffffff" stroke-width="2.5"/></svg>
</section>
<div class="hero-copy abs">
  <div class="line">Our firm specialises in the sale</div>
  <div class="line">of apartment properties in</div>
  <div class="place">Southern California</div>
</div>
<a class="btn-contact abs">Contact us</a>

<section class="approach abs">
  <h1 class="section-title">Our unique consultative approach</h1>
  <div class="subtitle heading">That uncovers unrealized opportunities</div>
  <p>Proin placerat dapibus gravida. In tristique tristique nulla eget hendrerit. Maecenas vel tortor accumsan quam varius imperdiet vel eget elit. Aenean facilisis tincidunt lectus, id dictum nisi luctus eget. Vivamus efficitur ex condimentum, malesuada eros eget, feugiat nibh. Sed tellus ex, imperdiet eget gravida sit amet, volutpat eget turpis. In nec ultricies est. Etiam mattis augue vehicula odio posuere, sit amet tempus lectus luctus. Nulla facilisi. Etiam vel massa elementum, bibendum tellus venenatis, feugiat massa. Curabitur venenatis lacinia ornare. Cras sollicitudin cursus dui eu placerat.</p>
</section>

<section class="features abs">
  <div class="feature abs" style="left:117px">
    <div class="feature-icon"><svg width="30" height="30" viewBox="0 0 30 30"><rect x="8" y="3" width="14" height="24" fill="none" stroke="#fff" stroke-width="2"/><g fill="#fff"><rect x="11" y="7" width="3" height="3"/><rect x="16" y="7" width="3" height="3"/><rect x="11" y="12" width="3" height="3"/><rect x="16" y="12" width="3" height="3"/><rect x="11" y="17" width="3" height="3"/><rect x="16" y="17" width="3" height="3"/><rect x="13" y="22" width="4" height="5"/></g></svg></div>
    <h3 class="heading">Aliquam erat</h3>
    <p>Aenean placerat, nibh vel ac accumsan aliquet, magna nibh accumsan nibh, ac tempus nunc ipsum ac tellus. Cras augue magna, placerat eget.</p>
  </div>
  <div class="feature abs" style="left:451px">
    <div class="feature-icon"><svg width="34" height="26" viewBox="0 0 34 26"><rect x="2" y="4" width="30" height="18" fill="none" stroke="#fff" stroke-width="2.5"/><circle cx="17" cy="13" r="5" fill="#fff"/></svg></div>
    <h3 class="heading">Phasellus nisl</h3>
    <p>Aenean placerat, nibh vel ac accumsan aliquet, magna nibh accumsan nibh, ac tempus nunc ipsum ac tellus. Cras augue magna, placerat eget.</p>
  </div>
  <div class="feature abs" style="left:785px">
    <div class="feature-icon"><svg width="34" height="30" viewBox="0 0 34 30"><path d="M2 3 V27 H32" fill="none" stroke="#fff" stroke-width="2"/><path d="M6 22 L13 14 L18 18 L28 8" fill="none" stroke="#fff" stroke-width="2.5"/><path d="M23 7 H29 V13" fill="none" stroke="#fff" stroke-width="2.5"/></svg></div>
    <h3 class="heading">Fusce eget</h3>
    <p>Aenean placerat, nibh vel ac accumsan aliquet, magna nibh accumsan nibh, ac tempus nunc ipsum ac tellus. Cras augue magna, placerat eget.</p>
  </div>
</section>

<h2 class="section-title projects-title abs">Our recent projects</h2>
<article class="project abs" style="left:132px">
  <div class="project-photo" role="img" aria-label="Curved white apartment tower with glass balconies" style="background:linear-gradient(135deg,#cfd6dc 0%,#8e9aa5 45%,#e8ecef 70%,#7d8a96 100%)"></div>
  <h3 class="heading">Donec vestibulum odio sem</h3>
  <p>Praesent iaculis faucibus urna sit amet lacinia. Maecenas consequat justo enim, ac mattis massa imperdiet quis. Fusce eget neque elit. Sed augue orci, elementum in magna congue, tincidunt vulputate erat.</p>
  <div class="btn-more">Read more</div>
</article>
<article class="project abs" style="left:450px">
  <div class="project-photo" role="img" aria-label="Red brick apartment block with white balconies" style="background:linear-gradient(135deg,#8fb7df 0%,#e3e3e3 30%,#b9462e 55%,#8a3322 80%,#d7d2cc 100%)"></div>
  <h3 class="heading">Curabitur ac elit leo</h3>
  <p>Praesent iaculis faucibus urna sit amet lacinia. Maecenas consequat justo enim, ac mattis massa imperdiet quis. Fusce eget neque elit. Sed augue orci, elementum in magna congue, tincidunt vulputate erat.</p>
  <div class="btn-more">Read more</div>
</article>
<article class="project abs" style="left:769px">
  <div class="project-photo" role="img" aria-label="Cream apartment building with dark iron balconies under a pale sky" style="background:linear-gradient(135deg,#9fd0e6 0%,#e9dcc0 40%,#c9a97a 65%,#4d4f55 100%)"></div>
  <h3 class="heading">Proin a dolor mauris</h3>
  <p>Praesent iaculis faucibus urna sit amet lacinia. Maecenas consequat justo enim, ac mattis massa imperdiet quis. Fusce eget neque elit. Sed augue orci, elementum in magna congue, tincidunt vulputate erat.</p>
  <div class="btn-more">Read more</div>
</article>

<section class="people abs">
  <h2 class="section-title people-title abs">Our people</h2>
  <svg class="slider-arrow abs" style="left:20px;top:165px" viewBox="0 0 20 30"><path d="M15 5 L6 15 L15 25" fill="none" stroke="#8a8f94" stroke-width="2.5"/></svg>
  <svg class="slider-arrow abs" style="left:1160px;top:165px" viewBox="0 0 20 30"><path d="M5 5 L14 15 L5 25" fill="none" stroke="#8a8f94" stroke-width="2.5"/></svg>
  <div class="person abs" style="left:133px"><div class="portrait" role="img" aria-label="Portrait of an adviser in a suit"></div><div class="name">Evan Hale</div><div class="role">Integer sapien felis</div></div>
  <div class="person abs" style="left:326px"><div class="portrait" role="img" aria-label="Portrait of an adviser" style="background:radial-gradient(circle at 50% 40%,#e2cbb8 0%,#a5532a 60%,#5a2f1d 100%)"></div><div class="name">Evan Hale</div><div class="role">Integer sapien felis</div></div>
  <div class="person abs" style="left:519px"><div class="portrait" role="img" aria-label="Portrait of an adviser in a suit"></div><div class="name">Evan Hale</div><div class="role">Integer sapien felis</div></div>
  <div class="person abs" style="left:712px"><div class="portrait" role="img" aria-label="Portrait of an adviser" style="background:radial-gradient(circle at 50% 40%,#f3e5d6 0%,#d8c29a 60%,#b9b3ab 100%)"></div><div class="name">Evan Hale</div><div class="role">Integer sapien felis</div></div>
  <div class="person abs" style="left:905px"><div class="portrait" role="img" aria-label="Portrait of an adviser in a suit"></div><div class="name">Evan Hale</div><div class="role">Integer sapien felis</div></div>
</section>

<section class="newsletter abs">
  <div class="newsletter-title abs"><svg width="30" height="24" viewBox="0 0 30 24"><rect x="2" y="2" width="26" height="20" fill="none" stroke="#fff" stroke-width="2.5"/><path d="M2 3 L15 14 L28 3" fill="none" stroke="#fff" stroke-width="2.5"/></svg>Newsletter</div>
  <div class="field abs" style="left:411px">Name</div>
  <div class="field abs" style="left:675px">Email</div>
  <div class="btn-subscribe abs">Subscribe</div>
</section>

<footer class="site-footer abs">
  <div class="footer-nav abs">Home<span class="sep">|</span>About Us<span class="sep">|</span>Projects<span class="sep">|</span>How we work?<span class="sep">|</span>Contact</div>
  <div class="copyright abs">Copyright © 2017 Meridian Advisers. All rights reserved.</div>
  <span class="social abs" style="left:937px"></span>
  <span class="social abs" style="left:973px"></span>
  <span class="social abs" style="left:1012px"></span>
  <span class="social abs" style="left:1052px"></span>
</footer>

</body>
</html>
```